Stonebrook 720 Real Estate Investment Company

We need a business card designed for a real estate investment company named Stonebrook 720. We want to use red#f04a50, orange #f37122 and yellow #fbee3e as the color scheme. The logo colors will need to be modified from the current blue palette. I've attach VitaPathway logo example that captures the color scheme we're going for for Stonebrook 720. Looking for clean Sans Serif fonts.
Contact Information for Business Card
Daniel Furlow
Managing Partner
48317 Whitfield Lane, Suite 510
Tampa, FL 33718
813-555-4870 Mobile
dfurlow@stonebrook720.example
www.stonebrook720.example
Requirements
Must have
- Looking for creative responses.
Nice to have
- Must hit color palette... orange, red, yellow

```html
<!DOCTYPE html>
<html lang="en">
<head>
<meta charset="utf-8">
<title>Stonebrook 720 — Business Card</title>
<link rel="stylesheet" href="https://fonts.googleapis.com/css2?family=Poppins:wght@400;500;700&display=swap">
<style>
  :root {
    --stage: #e9e7e4;
    --card: #141414;
    --card-edge: #1d1d1d;
    --gloss: #2b2b2b;
    --white: #ffffff;
    --muted: #e6e6e6;
    --red: #f04a50;
    --orange: #f37122;
    --yellow: #fbee3e;
    --divider: #bdbdbd;
  }
  * { box-sizing: border-box; margin: 0; padding: 0; }
  html, body { width: 1200px; height: 716px; overflow: hidden; }
  body {
    background: var(--stage);
    font-family: "Poppins", sans-serif;
    position: relative;
  }
  .card {
    position: absolute;
    top: 210px;
    width: 520px;
    height: 297px;
    background: var(--card);
    border: 1px solid var(--card-edge);
    border-radius: 4px;
    box-shadow: 0 6px 18px rgba(0,0,0,0.18);
    overflow: hidden;
  }
  .card--front { left: 50px; }
  .card--back { left: 630px; }

  /* Front */
  .front-mark {
    position: absolute;
    left: 50%;
    top: 50%;
    transform: translate(-50%, -50%);
    display: flex;
    align-items: center;
    gap: 14px;
  }
  .front-mark__name {
    font-weight: 700;
    font-size: 40px;
    letter-spacing: -0.5px;
    color: var(--gloss);
  }
  .front-mark__dot {
    width: 22px; height: 22px;
    border-radius: 50%;
    background: var(--gloss);
  }

  /* Back */
  .back-brand {
    position: absolute;
    left: 32px;
    top: 50%;
    transform: translateY(-50%);
    display: flex;
    align-items: center;
    gap: 8px;
  }
  .back-brand__name {
    font-weight: 700;
    font-size: 23px;
    letter-spacing: -0.3px;
    color: var(--white);
  }
  .back-brand__dot {
    width: 12px; height: 12px;
    border-radius: 50%;
    background: var(--red);
  }
  .divider {
    position: absolute;
    left: 245px;
    top: 62px;
    width: 1px;
    height: 172px;
    background: var(--divider);
  }
  .contact {
    position: absolute;
    left: 266px;
    top: 64px;
    color: var(--muted);
    font-size: 12.5px;
    line-height: 1.55;
  }
  .contact__name {
    color: var(--red);
    font-weight: 500;
    font-size: 19px;
    letter-spacing: 0.5px;
    text-transform: uppercase;
    line-height: 1.3;
  }
  .contact__title { margin-bottom: 2px; }
  .contact__row {
    display: flex;
    align-items: center;
    gap: 8px;
  }
  .contact__row svg { width: 11px; height: 11px; flex: none; }
</style>
</head>
<body>
  <section class="card card--front" aria-label="Card front">
    <div class="front-mark">
      <span class="front-mark__name">Stonebrook720</span>
      <span class="front-mark__dot"></span>
    </div>
  </section>

  <section class="card card--back" aria-label="Card back">
    <div class="back-brand">
      <span class="back-brand__name">Stonebrook720</span>
      <span class="back-brand__dot"></span>
    </div>
    <div class="divider"></div>
    <div class="contact">
      <p class="contact__name">Daniel Furlow</p>
      <p class="contact__title">Managing Partner</p>
      <p>48317 Whitfield Lane</p>
      <p>Suite 510 Tampa, FL 33718</p>
      <p class="contact__row">
        <svg viewBox="0 0 24 24" aria-hidden="true"><path fill="var(--red)" d="M6.6 10.8a15.2 15.2 0 0 0 6.6 6.6l2.2-2.2a1 1 0 0 1 1-.25 11.4 11.4 0 0 0 3.6.57 1 1 0 0 1 1 1V20a1 1 0 0 1-1 1A17 17 0 0 1 3 4a1 1 0 0 1 1-1h3.5a1 1 0 0 1 1 1c0 1.25.2 2.45.57 3.57a1 1 0 0 1-.25 1z"/></svg>
        813-555-4870
      </p>
      <p class="contact__row">
        <svg viewBox="0 0 24 24" aria-hidden="true"><rect x="2" y="5" width="20" height="14" rx="1" fill="none" stroke="var(--orange)" stroke-width="2.5"/><path d="M3 6l9 7 9-7" fill="none" stroke="var(--orange)" stroke-width="2.5"/></svg>
        dfurlow@stonebrook720.example
      </p>
      <p class="contact__row">
        <svg viewBox="0 0 24 24" aria-hidden="true"><circle cx="12" cy="12" r="9.5" fill="none" stroke="var(--yellow)" stroke-width="2.5"/><ellipse cx="12" cy="12" rx="4" ry="9.5" fill="none" stroke="var(--yellow)" stroke-width="2"/><path d="M3 12h18" stroke="var(--yellow)" stroke-width="2"/></svg>
        www.stonebrook720.example
      </p>
    </div>
  </section>
</body>
</html>
```